Modern Design Business Card industrial maintenance company

Business card design for Company named Brookvale Equipment Services

Target Market(s)

Industrial

Industry/Entity Type

Maintenance and repair

Contact Information for Business Card

Place holder for address, office phone, mobile number and email

Requirements
Must have
• Clean modern look
Nice to have
• N/a

```html
<!DOCTYPE html>
<html lang="en">
<head>
<meta charset="utf-8">
<title>Brookvale Equipment Services – Business Card</title>
<link rel="stylesheet" href="https://fonts.googleapis.com/css2?family=Montserrat:wght@300;400;600;700&display=swap">
<style>
  :root {
    --backdrop: #1e1e1e;
    --card: #121212;
    --ink: #ffffff;
    --ink-soft: #e6e6e6;
    --ring: #2c2c2c;
    --rule: #d8d8d8;
  }
  * { margin: 0; padding: 0; box-sizing: border-box; }
  html, body {
    width: 1200px; height: 1200px; overflow: hidden;
    background: var(--backdrop);
    font-family: "Montserrat", sans-serif;
    color: var(--ink);
  }
  .stage {
    position: relative; width: 1200px; height: 1200px;
    display: flex; justify-content: center; align-items: center; gap: 60px;
  }
  .card {
    width: 380px; height: 620px;
    background: var(--card);
    border-radius: 24px;
    position: relative;
    display: flex; flex-direction: column; align-items: center;
  }
  .brand { display: flex; flex-direction: column; align-items: center; margin-top: 52px; }
  .brand-circle {
    width: 72px; height: 72px; border-radius: 50%;
    border: 4px solid var(--ink); margin-bottom: 14px;
  }
  .brand-name {
    font-weight: 600; font-size: 19px; letter-spacing: 3px;
    text-transform: uppercase; text-align: center; line-height: 1.35;
    color: var(--ink);
  }
  .person { text-align: center; margin-top: 48px; }
  .person-name { font-weight: 700; font-size: 30px; letter-spacing: 1px; }
  .person-role { font-weight: 300; font-size: 19px; margin-top: 2px; }
  .contact-divider {
    display: flex; align-items: center; gap: 10px; width: 300px; margin-top: 34px;
  }
  .contact-divider .rule { flex: 1; height: 1px; background: var(--rule); }
  .icons { display: flex; gap: 8px; }
  .icon {
    width: 26px; height: 26px; background: var(--ink); border-radius: 6px;
    display: flex; align-items: center; justify-content: center;
  }
  .contacts {
    text-align: center; font-weight: 400; font-size: 17px; line-height: 1.55;
    margin-top: 12px; color: var(--ink-soft);
  }
  .rule-full { width: 300px; height: 1px; background: var(--rule); margin-top: 18px; }
  .address {
    text-align: center; font-weight: 400; font-size: 17px; line-height: 1.5;
    margin-top: 16px; color: var(--ink-soft);
  }
  .card-back { justify-content: space-between; }
  .back-ring {
    width: 300px; height: 300px; border-radius: 50%;
    border: 16px solid var(--ring); margin-top: 60px;
  }
  .back-brand { margin-bottom: 70px; }
  .back-brand .brand-name { font-size: 22px; }
</style>
</head>
<body>
<main class="stage">
  <section class="card card-front">
    <div class="brand">
      <div class="brand-circle"></div>
      <div class="brand-name">Brookvale<br>Equipment Services</div>
    </div>
    <div class="person">
      <div class="person-name">DANIEL HARWICK</div>
      <div class="person-role">Owner &amp; Manager</div>
    </div>
    <div class="contact-divider">
      <span class="rule"></span>
      <div class="icons">
        <span class="icon">
          <svg width="16" height="16" viewBox="0 0 24 24" aria-label="phone"><path fill="#121212" d="M6.6 10.8a15 15 0 0 0 6.6 6.6l2.2-2.2a1 1 0 0 1 1-.25 11.4 11.4 0 0 0 3.6.57 1 1 0 0 1 1 1V20a1 1 0 0 1-1 1A17 17 0 0 1 3 4a1 1 0 0 1 1-1h3.5a1 1 0 0 1 1 1c0 1.25.2 2.45.57 3.57a1 1 0 0 1-.25 1z"/></svg>
        </span>
        <span class="icon">
          <svg width="16" height="16" viewBox="0 0 24 24" aria-label="email"><rect x="3" y="5" width="18" height="14" rx="2" fill="#121212"/><path d="M3.5 6l8.5 7 8.5-7" stroke="#fff" stroke-width="1.8" fill="none"/></svg>
        </span>
        <span class="icon">
          <svg width="16" height="16" viewBox="0 0 24 24" aria-label="website"><circle cx="12" cy="12" r="9" fill="#121212"/><path d="M3 12h18M12 3c3 3 3 15 0 18M12 3c-3 3-3 15 0 18" stroke="#fff" stroke-width="1.4" fill="none"/></svg>
        </span>
      </div>
      <span class="rule"></span>
    </div>
    <div class="contacts">
      <div>5421 - 736 - 2208</div>
      <div>info@brookvaleequipment.com</div>
      <div>www.brookvaleequipment.com</div>
    </div>
    <div class="rule-full"></div>
    <div class="address">
      <div>P.O. Box Linden Street</div>
      <div>Country Name AB, T3K 2R7</div>
    </div>
  </section>

  <section class="card card-back">
    <div class="back-ring"></div>
    <div class="brand back-brand">
      <div class="brand-name">Brookvale<br>Equipment Services</div>
    </div>
  </section>
</main>
</body>
</html>
```